Byte Crew - Settle In

A flyer to promote a service by Byte Crew that provides IT set up in home when moving house.

It should be for print format (A4, A5 and an email friendly version)

Logos, previous flyer, image all attached.

Please use black, green and white as base colours.Please change boys sweater/jumper in the photo to green to match the logo.

Byte Crew are bring a helpdesk to your front door, saving you time and money. With a variety of packages to suit your needs, the Byte Crew aims to tackle both small and complex issues from setting up a home network to servicing the needs of a growing company.

Target Market(s)

Consumers moving house, Relocation agents, Real Estate agents

Requirements
Must have
• Logo, image, text all attached
• Use of green, black and white
Nice to have
• Also have coloured ties if you want them for design

```html
<!DOCTYPE html>
<html lang="en">
<head>
<meta charset="utf-8">
<title>Byte Crew – Settle In flyer</title>
<link rel="stylesheet" href="https://fonts.googleapis.com/css2?family=Anton&family=Archivo+Black&family=Arimo:wght@400;700&family=Mulish:wght@400;800&display=swap">
<style>
  :root {
    --ink: #231f20;
    --green: #7dc242;
    --white: #ffffff;
    --yellow: #f7ec1a;
    --yellow-edge: #c25a12;
    --photo-a: #5c7f86;
    --photo-b: #c9b39a;
    --photo-c: #6f9a58;
  }
  * { margin: 0; padding: 0; box-sizing: border-box; }
  html, body { width: 852px; height: 1200px; overflow: hidden; background: var(--white); }
  .flyer { position: relative; width: 852px; height: 1200px; background: var(--white); overflow: hidden; }

  .hero-photo {
    position: absolute; left: 0; top: 0; width: 852px; height: 466px;
    background:
      radial-gradient(ellipse 260px 230px at 560px 170px, var(--photo-b), transparent 70%),
      radial-gradient(ellipse 400px 120px at 480px 440px, var(--photo-c), transparent 75%),
      linear-gradient(135deg, #8aa7a9, var(--photo-a) 55%, #3d5559);
  }
  .hero-headline {
    position: absolute; left: 22px; top: 12px;
    font-family: "Archivo Black", "Arial Black", sans-serif;
    color: var(--yellow); -webkit-text-stroke: 2px var(--yellow-edge);
    line-height: 0.9; letter-spacing: 1px;
  }
  .hero-headline .line-1 { display: block; font-size: 78px; }
  .hero-headline .line-1 .stress { font-size: 104px; }
  .hero-headline .line-2 { display: block; font-size: 104px; margin-top: -6px; }

  .rule { position: absolute; left: 0; width: 852px; height: 4px; background: var(--green); }

  .intro-band { position: absolute; left: 0; top: 470px; width: 852px; height: 214px; background: var(--ink); }
  .brand-line { font-family: "Arimo", Arial, sans-serif; font-weight: 700; color: var(--white); }
  .brand-line .lead { position: absolute; left: 8px; top: 8px; font-size: 42px; }
  .brand-line .brand { position: absolute; left: 90px; top: 18px; font-size: 66px; white-space: nowrap; }
  .brand-line .brand-mark { display: inline-block; width: 16px; height: 16px; background: var(--green); margin-right: 10px; }
  .brand-line .tail { position: absolute; left: 440px; top: 64px; font-size: 42px; }
  .tagline {
    position: absolute; left: 0; top: 128px; width: 852px; text-align: center;
    font-family: "Arimo", Arial, sans-serif; font-size: 32px; line-height: 37px; color: var(--green);
  }

  .offer-area { position: absolute; left: 0; top: 688px; width: 852px; height: 330px; background: var(--ink); }
  .services {
    position: absolute; left: 0; top: 10px; width: 852px; text-align: center;
    font-family: "Arimo", Arial, sans-serif; font-size: 15px; line-height: 20px; color: var(--white);
  }
  .offer-shapes { position: absolute; left: 0; top: 0; }
  .promise {
    position: absolute; left: 5px; top: 98px; width: 440px; text-align: center;
    font-family: "Mulish", "Century Gothic", sans-serif; color: var(--ink);
    font-size: 31px; line-height: 41px;
  }
  .promise strong { font-weight: 800; font-size: 35px; line-height: 46px; display: block; }
  .price {
    position: absolute; left: 448px; top: 150px; width: 400px; text-align: center;
    font-family: "Arimo", Arial, sans-serif; color: var(--white);
  }
  .price .price-title { font-weight: 700; font-size: 39px; line-height: 48px; }
  .price .price-amount { font-size: 28px; line-height: 38px; }

  .signup-band { position: absolute; left: 0; top: 1022px; width: 852px; height: 168px; background: var(--ink); text-align: center; }
  .signup {
    position: absolute; left: 0; top: 18px; width: 852px;
    font-family: "Anton", Impact, sans-serif; font-size: 50px; color: var(--white); letter-spacing: 0.5px;
  }
  .signup .web { color: var(--green); }
  .contact {
    position: absolute; left: 0; top: 92px; width: 852px;
    font-family: "Mulish", "Century Gothic", sans-serif; font-size: 29px; color: var(--white);
  }
  .contact b { font-weight: 800; }
  .footnote {
    position: absolute; right: 16px; top: 146px;
    font-family: "Arimo", Arial, sans-serif; font-size: 14px; color: var(--white);
  }
</style>
</head>
<body>
<main class="flyer">
  <div class="hero-photo" role="img" aria-label="Photo of a worried boy in glasses and a green jumper gingerly holding a network cable after a move"></div>
  <h1 class="hero-headline">
    <span class="line-1">Do <span class="stress">not</span></span>
    <span class="line-2">fear...</span>
  </h1>

  <div class="rule" style="top:466px"></div>
  <section class="intro-band">
    <p class="brand-line">
      <span class="lead">the</span>
      <span class="brand"><span class="brand-mark"></span>Byte Crew</span>
      <span class="tail">is here!</span>
    </p>
    <p class="tagline">We take the Heavy lifting out of moving your IT by<br>bringing a help desk to your new front door</p>
  </section>
  <div class="rule" style="top:684px"></div>

  <section class="offer-area">
    <svg class="offer-shapes" width="852" height="330" viewBox="0 0 852 330" aria-hidden="true">
      <path d="M5 102 H360 V60 H445 V330 H5 Z" fill="var(--green)"/>
      <rect x="760" y="8" width="92" height="110" fill="var(--green)"/>
      <rect x="593" y="84" width="84" height="32" fill="var(--green)"/>
      <rect x="446" y="115" width="402" height="208" rx="18" fill="var(--ink)" stroke="var(--green)" stroke-width="2"/>
    </svg>
    <p class="services">Just moved? Back up your data and photos, connect devices still sitting in moving boxes,<br>check your software is the latest and greatest, and get your new home network running.</p>
    <p class="promise">Whatever the cry for help -<strong>no request is<br>too BIG or small.</strong>The Byte Crew has seen<br>and solved them all.</p>
    <div class="price">
      <p class="price-title">Back up, Tune up<br>&amp; Protect</p>
      <p class="price-amount">from only $48 a month*</p>
    </div>
  </section>

  <div class="rule" style="top:1018px"></div>
  <footer class="signup-band">
    <p class="signup">Sign up at <span class="web">www.bytecrew.asia</span></p>
    <p class="contact">Singapore hotline <b>6123 4587</b> &nbsp;|&nbsp; email <b>info@bytecrew.asia</b></p>
    <p class="footnote">*Settle In package, based on a 12 month contract in Singapore</p>
  </footer>
  <div class="rule" style="top:1190px"></div>
</main>
</body>
</html>
```